Letterhead/Busines Cards for Harborview Psychiatry, PLLC - modern psychiatric practice
Harborview Psychiatry, PLLC
Professional
Gerald Matthis, MSN, APRN, PMHNP-BC
President
5812 Quailrun Lane
Lexington, KY 40509
tkwarden4@mailvista.example
please design leaving out black background

```html
<!DOCTYPE html>
<html lang="en">
<head>
<meta charset="utf-8">
<title>Harborview Psychiatry, PLLC – Business Card</title>
<link rel="stylesheet" href="https://fonts.googleapis.com/css2?family=Open+Sans:wght@400;600;700&display=swap">
<style>
  :root {
    --page-bg: #dcd8d1;
    --card-bg: #f8f6f2;
    --card-edge: #cfc9bf;
    --gold-light: #f3b25a;
    --gold-mid: #d98c2b;
    --gold-dark: #a8621a;
    --brand-gold: #bf7624;
    --rule-grey: #8a8a8d;
    --text-body: #3c3c3f;
    --name-dark: #2a2014;
    --icon-glyph: #ffffff;
  }
  * { margin: 0; padding: 0; box-sizing: border-box; }
  html, body {
    width: 1200px; height: 914px; overflow: hidden;
    background: var(--page-bg);
    font-family: "Open Sans", Arial, sans-serif;
  }
  .business-card {
    position: absolute; left: 100px; top: 171px;
    width: 1000px; height: 572px;
    background: var(--card-bg);
    border: 1px solid var(--card-edge);
    box-shadow: 0 6px 18px rgba(0,0,0,0.12);
  }
  .brand {
    position: absolute; top: 150px; left: 0; width: 100%;
    display: flex; align-items: center; justify-content: center; gap: 18px;
  }
  .brand-dot {
    width: 26px; height: 26px; border-radius: 50%;
    background: var(--gold-mid);
  }
  .brand-name {
    font-weight: 700; font-size: 44px; letter-spacing: 0.5px;
    color: var(--brand-gold);
  }
  .title-band {
    position: absolute; left: 0; top: 318px; width: 100%; height: 56px;
    background: linear-gradient(90deg, var(--gold-dark) 0%, var(--gold-mid) 30%, var(--gold-light) 55%, var(--gold-mid) 80%, var(--gold-dark) 100%);
    border-top: 3px solid var(--rule-grey);
    border-bottom: 3px solid var(--rule-grey);
    display: flex; align-items: center; justify-content: center;
  }
  .holder-line {
    font-weight: 700; font-size: 24px; color: var(--name-dark);
    white-space: nowrap;
  }
  .contact-list {
    position: absolute; left: 140px; top: 404px; width: 760px;
    font-size: 17px; color: var(--text-body);
  }
  .contact-row { display: flex; gap: 34px; margin-bottom: 12px; }
  .contact-item { display: flex; align-items: center; gap: 8px; white-space: nowrap; }
  .contact-icon { width: 18px; height: 18px; flex: none; }
</style>
</head>
<body>
  <div class="business-card">
    <div class="brand">
      <span class="brand-dot"></span>
      <span class="brand-name">Harborview Psychiatry, PLLC</span>
    </div>

    <div class="title-band">
      <p class="holder-line">Gerald Matthis, MSN, APRN, PMHNP-BC | President</p>
    </div>

    <div class="contact-list">
      <div class="contact-row">
        <span class="contact-item">
          <svg class="contact-icon" viewBox="0 0 18 18"><circle cx="9" cy="9" r="9" fill="#d98c2b"/><path d="M9 4a3.2 3.2 0 0 0-3.2 3.2C5.8 10 9 14 9 14s3.2-4 3.2-6.8A3.2 3.2 0 0 0 9 4zm0 4.4a1.2 1.2 0 1 1 0-2.4 1.2 1.2 0 0 1 0 2.4z" fill="#ffffff"/></svg>
          5812 Quailrun Lane Lexington, KY 40509
        </span>
        <span class="contact-item">
          <svg class="contact-icon" viewBox="0 0 18 18"><circle cx="9" cy="9" r="9" fill="#d98c2b"/><circle cx="9" cy="9" r="4.5" fill="none" stroke="#ffffff" stroke-width="1.3"/><path d="M4.5 9h9M9 4.5c-2 2.5-2 6.5 0 9M9 4.5c2 2.5 2 6.5 0 9" fill="none" stroke="#ffffff" stroke-width="1.1"/></svg>
          www.harborviewpsych.example
        </span>
      </div>
      <div class="contact-row">
        <span class="contact-item">
          <svg class="contact-icon" viewBox="0 0 18 18"><circle cx="9" cy="9" r="9" fill="#d98c2b"/><path d="M6 4.5l1.8 2.6-1 1.1a6.5 6.5 0 0 0 3 3l1.1-1 2.6 1.8-1 1.6C9 13.6 4.4 9 4.4 5.5z" fill="#ffffff"/></svg>
          (606) 555-0182
        </span>
        <span class="contact-item">
          <svg class="contact-icon" viewBox="0 0 18 18"><circle cx="9" cy="9" r="9" fill="#d98c2b"/><path d="M6 4.5l1.8 2.6-1 1.1a6.5 6.5 0 0 0 3 3l1.1-1 2.6 1.8-1 1.6C9 13.6 4.4 9 4.4 5.5z" fill="#ffffff"/></svg>
          (606) 555-0147
        </span>
        <span class="contact-item">
          <svg class="contact-icon" viewBox="0 0 18 18"><circle cx="9" cy="9" r="9" fill="#d98c2b"/><rect x="4.5" y="5.8" width="9" height="6.4" fill="none" stroke="#ffffff" stroke-width="1.3"/><path d="M4.5 5.8L9 9.6l4.5-3.8" fill="none" stroke="#ffffff" stroke-width="1.2"/></svg>
          tkwarden4@mailvista.example
        </span>
      </div>
    </div>
  </div>
</body>
</html>
```